Tech Company Start-up complete branding (Logo, flyer, stationary and Website)

We need a logo, product/services flyer template, Stationary and website with 6 unique templates.

Logo:

Option A.) Technology Enabled New-Look Corvane with Security in-mind. (with the icon being the umbrella). Please create a NEW umbrella that resembles the ‘physical-form’ of a traditional umbrella but a
Option B.) No Icon or symbol (umbrella) just the characters.

We are a service installing technology system integration company. Our focus is video surveillance, access-control, cyber security, fire and burglar alarms, monitoring and managed services.

What is the purpose of this site?

This section should include an overview of what the general purpose and goal of the web site is. Please put an X (next to the ones that apply to you (OR) Bold Fonts.

- Explain your products and services
- Bring in new clients to your business
- Provide your customers with information on a certain subject
- Deliver news or calendar of events
- Provide support for current clients

We deliver solution based project engineering with superior technology
knowledge, design and service. Corvane is the most cost effective team to
protect your people, assets and infrastructure.

Target Market(s)

End users of commercial or government facilities: Global, Male : 30-55.

Industry/Entity Type

Technical Service

Contact Information for Business Card

Simple, Elegant

Logo Text

'Corvane Technologies' or 'Corvane Tech'

Number of Pages Required

4 page

Requirements
Must have
• Website:
• 100% Responsive (Mobile, Desktop, Tablet)
• Paralax capabilities
• Must be built on Wordpress with CRM
• Stickey Navigation on scroll
• Home Page must have ability to have video start @ top or change to 2/3 sliders
• ***WE must be able to updated the site and grow it our selves upon completion of the project (Changing text, adding/subtracting pages, Adding/subtracting images***
• No text embedded in images
• Built-In Blog Template with our branding
• Built-In SEO
Nice to have
• Built-In options for addtional page templates

```html
<!DOCTYPE html>
<html lang="en">
<head>
<meta charset="utf-8">
<title>Corvane Technologies — Stationery</title>
<link href="https://fonts.googleapis.com/css2?family=Questrial&display=swap" rel="stylesheet">
<style>
  :root {
    --ink: #1a1a1a;
    --charcoal: #3d3d3d;
    --paper: #ffffff;
    --accent: #29abe2;
    --muted: #333333;
    --light-text: #e8e8e8;
    --shadow: rgba(0, 0, 0, 0.35);
  }
  * { margin: 0; padding: 0; box-sizing: border-box; }
  html, body {
    width: 1200px; height: 720px; overflow: hidden;
    background: var(--paper);
    font-family: "Questrial", "Century Gothic", sans-serif;
    color: var(--ink);
  }
  .stage { position: relative; width: 1200px; height: 720px; }

  /* Letterhead */
  .letterhead {
    position: absolute; left: 48px; top: 14px; width: 476px; height: 672px;
    background: var(--paper);
    box-shadow: 5px 6px 8px var(--shadow);
  }
  .letterhead__bar { height: 8px; background: var(--charcoal); }
  .letterhead__brand { position: absolute; left: 14px; top: 58px; }
  .letterhead__contact { position: absolute; left: 344px; top: 26px; font-size: 9.5px; color: var(--muted); }
  .letterhead__footer {
    position: absolute; left: 0; bottom: 18px; width: 209px; height: 30px;
    background: var(--charcoal); border-radius: 0 15px 15px 0;
    color: var(--light-text); font-size: 12px; letter-spacing: .3px;
    display: flex; align-items: center; padding-left: 36px;
  }

  /* Brand name */
  .brand { display: flex; align-items: center; gap: 8px; }
  .brand__mark { width: 12px; height: 12px; background: var(--accent); flex: none; }
  .brand__name { font-weight: 400; color: var(--ink); white-space: nowrap; line-height: 1; }
  .brand--small .brand__name { font-size: 22px; }
  .brand--large .brand__name { font-size: 27px; }
  .brand--large .brand__mark { width: 14px; height: 14px; }
  .brand--light .brand__name { color: #ffffff; font-size: 18px; }
  .brand--light .brand__mark { width: 10px; height: 10px; }

  /* Contact lists */
  .contact-list { list-style: none; }
  .contact-list li { display: flex; align-items: flex-start; gap: 10px; }
  .contact-list svg { flex: none; fill: var(--accent); }
  .letterhead__contact li { margin-bottom: 12px; line-height: 1.3; }
  .letterhead__contact svg { width: 11px; height: 11px; margin-top: 1px; }

  /* Business cards */
  .card {
    position: absolute; top: 256px; width: 364px; height: 235px;
    box-shadow: 5px 6px 8px var(--shadow);
    overflow: hidden;
  }
  .card--front { left: 379px; background: var(--paper); display: flex; align-items: center; justify-content: center; }
  .card--back { left: 768px; background: var(--charcoal); color: var(--light-text); }
  .card__brand { position: absolute; left: 14px; top: 110px; }
  .card__rule {
    position: absolute; left: 0; top: 142px; width: 150px; height: 2px;
    background: linear-gradient(to right, var(--accent), rgba(41,171,226,0));
  }
  .card__contact { position: absolute; left: 198px; top: 76px; font-size: 11px; }
  .card__contact li { margin-bottom: 10px; line-height: 1.3; }
  .card__contact svg { width: 13px; height: 13px; margin-top: 1px; }
</style>
</head>
<body>
<main class="stage">

  <section class="letterhead" aria-label="Letterhead">
    <div class="letterhead__bar"></div>
    <div class="letterhead__brand brand brand--small">
      <span class="brand__mark"></span>
      <span class="brand__name">Corvane Technologies</span>
    </div>
    <ul class="letterhead__contact contact-list">
      <li>
        <svg viewBox="0 0 16 16" aria-hidden="true"><path d="M8 1 0 8h2v7h4v-5h4v5h4V8h2z"/></svg>
        <span>402 Maple Crest Avenue<br>Fairhaven, HI 70312</span>
      </li>
      <li>
        <svg viewBox="0 0 16 16" aria-hidden="true"><path d="M1 3h14v10H1z"/><path d="M1.5 3.5 8 9l6.5-5.5" fill="none" stroke="#fff" stroke-width="1.3"/></svg>
        <span>info@corvanetech.com</span>
      </li>
      <li>
        <svg viewBox="0 0 16 16" aria-hidden="true"><path d="M4 0h8a1 1 0 0 1 1 1v14a1 1 0 0 1-1 1H4a1 1 0 0 1-1-1V1a1 1 0 0 1 1-1zm1 2v10h6V2z"/></svg>
        <span>555 - 014 -2290</span>
      </li>
    </ul>
    <div class="letterhead__footer">www.corvanetech.com</div>
  </section>

  <section class="card card--front" aria-label="Business card front">
    <div class="brand brand--large">
      <span class="brand__mark"></span>
      <span class="brand__name">Corvane Technologies</span>
    </div>
  </section>

  <section class="card card--back" aria-label="Business card back">
    <div class="card__brand brand brand--light">
      <span class="brand__mark"></span>
      <span class="brand__name">Corvane Tech</span>
    </div>
    <div class="card__rule"></div>
    <ul class="card__contact contact-list">
      <li>
        <svg viewBox="0 0 16 16" aria-hidden="true"><path d="M8 1 0 8h2v7h4v-5h4v5h4V8h2z"/></svg>
        <span>402 Maple Crest Avenue<br>Fairhaven, HI 70312</span>
      </li>
      <li>
        <svg viewBox="0 0 16 16" aria-hidden="true"><path d="M1 3h14v10H1z"/><path d="M1.5 3.5 8 9l6.5-5.5" fill="none" stroke="var(--charcoal)" stroke-width="1.3"/></svg>
        <span>info@corvanetech.com</span>
      </li>
      <li>
        <svg viewBox="0 0 16 16" aria-hidden="true"><g fill="none" stroke="var(--accent)" stroke-width="1.3"><circle cx="8" cy="8" r="6.5"/><ellipse cx="8" cy="8" rx="3" ry="6.5"/><path d="M1.5 8h13M2.5 4.5h11M2.5 11.5h11"/></g></svg>
        <span>www.corvanetech.com</span>
      </li>
      <li>
        <svg viewBox="0 0 16 16" aria-hidden="true"><path d="M4 0h8a1 1 0 0 1 1 1v14a1 1 0 0 1-1 1H4a1 1 0 0 1-1-1V1a1 1 0 0 1 1-1zm1 2v10h6V2z"/></svg>
        <span>555 - 014 -2290</span>
      </li>
    </ul>
  </section>

</main>
</body>
</html>
```